Health Focused Company Looking For New Bag Design For Capsules

We are revamping our our old plastic bag. We want this bag to really pop and look very modern. Anything goes. But there are a few things...

Must be our colors (logo attached)
Must have similar text to our old bag (old bag image attached)
Must have UPC somewhere on it (attached)
Must highlight that we are now putting in 2 bags in the main bag. More on this below... (explainer image attached)

We are splitting our capsules so they will be separated in the main bag (the one you are designing). There will be 2 smaller bags in the larger bag. One will be filled with only tops of the capsules and the other will be filled with only bottoms. Then both will be in the larger bag you will design. We want to highlight this prominently on the outside bag so people know right away by looking at it.

We also want to make sure KQM Approved, Halal and Kosher are kept very visible.

```html
<!DOCTYPE html>
<html lang="en">
<head>
<meta charset="utf-8">
<title>Solvara Gelatin Capsules Bag</title>
<link rel="stylesheet" href="https://fonts.googleapis.com/css2?family=Open+Sans:wght@400;600;700&display=swap">
<style>
  :root {
    --page-bg: #f1f1f3;
    --navy-deep: #22236f;
    --navy: #3a3ba0;
    --navy-text: #2e2f8f;
    --swoosh: #4f9fd6;
    --panel-top: #ffffff;
    --panel-bottom: #eee3ec;
    --lavender: #b9c1df;
    --capsule-fill: #f2dcc3;
    --capsule-shade: #e9c9a6;
    --brand-green: #8cc152;
    --badge-green: #4caf3a;
    --white: #ffffff;
  }
  html, body {
    margin: 0;
    padding: 0;
    width: 1200px;
    height: 1166px;
    overflow: hidden;
    background: var(--page-bg);
    font-family: "Open Sans", Arial, sans-serif;
  }
  .bag {
    position: absolute;
    left: 228px;
    top: 63px;
    width: 744px;
    height: 1040px;
  }
  .bag svg { display: block; }
  .brand-name { font-family: "Open Sans", Arial, sans-serif; font-weight: 400; fill: var(--brand-green); }
  .feature-title { font-family: "Open Sans", Arial, sans-serif; font-weight: 700; fill: var(--navy-text); }
  .count-line { font-family: "Open Sans", Arial, sans-serif; font-weight: 600; fill: var(--navy-text); }
  .ingredients-label { font-family: "Open Sans", Arial, sans-serif; font-weight: 600; fill: var(--navy-text); }
  .ingredients-list { font-family: "Open Sans", Arial, sans-serif; font-weight: 700; fill: var(--navy-text); }
  .certifications { font-family: "Open Sans", Arial, sans-serif; font-weight: 600; fill: var(--navy-text); }
  .no-additives { font-family: "Open Sans", Arial, sans-serif; font-weight: 400; fill: var(--navy-text); }
</style>
</head>
<body>
<div class="bag">
  <svg width="744" height="1040" viewBox="0 0 744 1040" xmlns="http://www.w3.org/2000/svg">
    <defs>
      <linearGradient id="bag-body" x1="0" y1="0" x2="0" y2="1">
        <stop offset="0" stop-color="var(--navy-deep)"/>
        <stop offset="0.12" stop-color="var(--navy-deep)"/>
        <stop offset="0.35" stop-color="var(--navy)"/>
        <stop offset="1" stop-color="var(--navy)"/>
      </linearGradient>
      <linearGradient id="label-panel" x1="0" y1="0" x2="0" y2="1">
        <stop offset="0" stop-color="var(--panel-top)"/>
        <stop offset="1" stop-color="var(--panel-bottom)"/>
      </linearGradient>
      <linearGradient id="capsule-window" x1="0" y1="0" x2="1" y2="1">
        <stop offset="0" stop-color="var(--capsule-fill)"/>
        <stop offset="1" stop-color="var(--capsule-shade)"/>
      </linearGradient>
    </defs>

    <!-- bag body -->
    <rect class="bag-body" x="0" y="0" width="744" height="1040" fill="url(#bag-body)"/>

    <!-- swoosh band -->
    <path class="swoosh-band" d="M0,660 C180,455 420,300 744,272 L744,302 C420,332 180,485 0,676 Z" fill="var(--swoosh)"/>

    <!-- label panel -->
    <path class="label-panel" d="M0,676 C180,485 420,332 744,302 L744,1040 L0,1040 Z" fill="url(#label-panel)"/>

    <!-- ingredients band -->
    <rect class="ingredients-band" x="0" y="872" width="744" height="168" fill="var(--lavender)"/>
    <rect class="bottom-edge" x="0" y="1032" width="744" height="8" fill="var(--navy)"/>

    <!-- tear notches -->
    <circle class="notch" cx="0" cy="96" r="7" fill="var(--white)"/>
    <circle class="notch" cx="744" cy="96" r="7" fill="var(--white)"/>
    <circle class="notch" cx="0" cy="976" r="20" fill="var(--white)"/>
    <circle class="notch" cx="744" cy="976" r="20" fill="var(--white)"/>

    <!-- tops window -->
    <path class="capsule-window" role="img" aria-label="Window showing the clear capsule tops inside"
          d="M296,376 V232 A65.5,65.5 0 0 1 427,232 V376 Z"
          fill="url(#capsule-window)" stroke="var(--white)" stroke-width="6"/>

    <!-- bottoms window -->
    <path class="capsule-window" role="img" aria-label="Window showing the clear capsule bottoms inside"
          d="M299,672 V814 A64,64 0 0 0 427,814 V672 Z"
          fill="url(#capsule-window)" stroke="var(--navy-text)" stroke-width="5"/>

    <!-- brand -->
    <circle class="brand-dot" cx="408" cy="470" r="14" fill="var(--brand-green)"/>
    <text class="brand-name" x="408" y="542" font-size="54" text-anchor="middle">solvara</text>

    <!-- feature -->
    <line class="rule" x1="168" y1="566" x2="587" y2="566" stroke="var(--navy-text)" stroke-width="3"/>
    <text class="feature-title" x="378" y="593" font-size="26" text-anchor="middle">SEPARATED TOPS&amp;BOTTOMS</text>
    <line class="rule" x1="168" y1="605" x2="587" y2="605" stroke="var(--navy-text)" stroke-width="3"/>
    <text class="count-line" x="378" y="648" font-size="28" text-anchor="middle">1000 Size "OO" Gelatin Capsules</text>

    <!-- natural badge -->
    <circle class="badge" cx="638" cy="757" r="58" fill="var(--white)" stroke="var(--badge-green)" stroke-width="6"/>
    <circle class="badge-inner" cx="638" cy="757" r="44" fill="none" stroke="var(--badge-green)" stroke-width="3"/>

    <!-- ingredients -->
    <text class="ingredients-label" x="400" y="925" font-size="20" text-anchor="middle">ingredients:</text>
    <text class="ingredients-list" x="400" y="962" font-size="31" text-anchor="middle">Beef Gelatin and Water</text>
    <text class="certifications" x="400" y="991" font-size="18" text-anchor="middle">Kosher, Halal and KQM approved</text>
    <text class="no-additives" x="400" y="1020" font-size="21" text-anchor="middle">No preservatives or additives</text>
  </svg>
</div>
</body>
</html>
```